依頼詳細
清潔感のあるイメージを希望しています。
できれば安心感を与える為、女性の写真などをいれてください。
掲載してもらいたい内容を載せています
宜しくお願いします。
①24時間営業
②6/6(金)新規オープン
③アクセスマップ(わかりにくい場所にあるので大きめに作成してください)
④6/30まで全機種半額
洗濯乾燥8kg 800円→400円
洗濯乾燥15kg 1000円→500円
洗濯のみ12kg 400円→200円
洗濯のみ22kg 600円→300円
乾燥のみ14kg 100円/11分→100円/22分
乾燥のみ25kg 100円/9分→100円/18分
⑤洗濯機から乾燥機に移す面倒な手間いらずの全自動洗濯乾燥機を導入
⑥となりのふとんクリーニング工場プロデュースなので
羽毛布団、こたつ布団、毛布の洗濯も安心
スタッフが工場に常駐なので安心
記載項目
社名(さらり堂コインランドリー)、住所(大分市椿原427-5)、地図(添付ファイル、キャラクターぴかりん、店舗写真、店内写真
サイズ
A4
ページ数
両面
希望イメージ
シンプル 複雑
単色 カラフル
暗い 明るい
日常 高級
遊び心 厳粛
未来的 伝統的
女性的 男性的
希望する色
納品ファイル
• 高解像度JPG (.jpg)
• イラストレーター形式 (.ai)
• フォトショップ形式 (.psd)
補足説明
店舗写真は添付の工場写真を当て込んでください。店内写真もまだ用意できていませんので空欄でお願いします。正式な写真は後日差し替えをお願いします。
添付の地図に近郊のお客様の目印になりそうな店名を追記しています。参考にしてください。場所が奥まっていますので地図は大きめに詳しく表記をお願いします。
納品はアウトライン化したものとしていないものの両方お願いします。
写真等のデータファイルを追加します
宜しくお願いします

```html
<!DOCTYPE html>
<html lang="ja">
<head>
<meta charset="utf-8">
<title>さらり堂コインランドリー 6月6日オープン</title>
<link href="https://fonts.googleapis.com/css2?family=Noto+Sans+JP:wght@500;700;900&family=M+PLUS+Rounded+1c:wght@800;900&display=swap" rel="stylesheet">
<style>
  :root {
    --red: #d7101e;
    --deep-red: #b30a16;
    --white: #ffffff;
    --yellow: #ffe33a;
    --sky-top: #2f7fd0;
    --sky-mid: #7db8ea;
    --sky-low: #dfeefa;
    --ink: #222222;
  }
  * { margin: 0; padding: 0; box-sizing: border-box; }
  html, body { width: 848px; height: 1200px; overflow: hidden; background: var(--white); }
  .flyer {
    position: relative; width: 848px; height: 1200px; overflow: hidden;
    font-family: "Noto Sans JP", sans-serif; color: var(--ink);
  }
  .hero-photo {
    position: absolute; left: 0; top: 0; width: 848px; height: 740px;
    background:
      radial-gradient(ellipse 300px 380px at 600px 380px, #f3ece4 0%, #e8dccf 45%, rgba(232,220,207,0) 75%),
      linear-gradient(180deg, var(--sky-top) 0%, var(--sky-mid) 45%, var(--sky-low) 100%);
  }
  .date {
    position: absolute; left: 70px; top: 14px;
    font-family: "M PLUS Rounded 1c", sans-serif; font-weight: 900;
    font-size: 104px; line-height: 1; color: var(--red);
    text-shadow: 4px 0 var(--white), -4px 0 var(--white), 0 4px var(--white), 0 -4px var(--white), 3px 3px var(--white), -3px -3px var(--white), 3px -3px var(--white), -3px 3px var(--white);
    letter-spacing: -2px;
  }
  .date .unit { font-size: 80px; }
  .weekday {
    position: absolute; left: 470px; top: 40px; width: 70px; height: 70px;
    border-radius: 50%; background: var(--red); border: 4px solid var(--white);
    color: var(--white); font-weight: 900; font-size: 40px;
    display: flex; align-items: center; justify-content: center;
  }
  .open {
    position: absolute; left: 72px; top: 118px;
    font-weight: 900; font-size: 124px; line-height: 1; color: var(--red); letter-spacing: 2px;
    text-shadow: 5px 0 var(--white), -5px 0 var(--white), 0 5px var(--white), 0 -5px var(--white), 4px 4px var(--white), -4px -4px var(--white), 4px -4px var(--white), -4px 4px var(--white);
  }
  .shop-banner {
    position: absolute; left: 120px; top: 256px; width: 700px; height: 160px;
    background: var(--red); border: 5px solid var(--white); border-radius: 18px;
    color: var(--white); padding: 14px 0 0 44px;
  }
  .shop-banner .shop-name { font-weight: 700; font-size: 38px; line-height: 1.1; padding-left: 16px; }
  .shop-banner .shop-kind { font-weight: 900; font-size: 76px; line-height: 1.25; white-space: nowrap; }
  .sale-badge {
    position: absolute; left: 8px; top: 405px; width: 300px; height: 300px;
    border-radius: 50%; background: var(--white); border: 7px solid var(--red);
    text-align: center; overflow: hidden;
  }
  .sale-badge .until { margin-top: 52px; font-weight: 900; font-size: 46px; color: var(--red); line-height: 1.05; }
  .sale-badge .scope { font-weight: 900; font-size: 46px; color: var(--red); line-height: 1.1; }
  .sale-badge .half {
    margin-top: 8px; background: var(--yellow);
    font-family: "M PLUS Rounded 1c", sans-serif; font-weight: 900;
    font-size: 92px; line-height: 108px; color: var(--red); letter-spacing: 8px;
  }
  .mascot {
    position: absolute; left: 625px; top: 430px; width: 190px; height: 210px;
    border-radius: 46% 46% 40% 40%; background: linear-gradient(180deg, #e23a3a, #c51b1b 70%, #f6f1ea 70%);
  }
  .mascot-name {
    position: absolute; left: 625px; top: 645px; width: 190px; text-align: center;
    font-weight: 700; font-size: 24px; color: var(--ink);
  }
  .feature-band {
    position: absolute; left: 0; top: 722px; width: 848px; height: 256px; background: var(--red);
  }
  .store-photo {
    position: absolute; left: 14px; top: 732px; width: 356px; height: 234px;
    background: linear-gradient(180deg, #b8d4ee 0%, #e9eef2 45%, #d9d2c8 60%, #9a8f86 100%);
    border: 3px solid var(--white);
  }
  .feature {
    position: absolute; top: 724px; width: 200px; height: 200px; border-radius: 50%;
    background: var(--white); border: 6px solid var(--red); box-shadow: 0 0 0 4px var(--white);
    display: flex; flex-direction: column; align-items: center; justify-content: center;
    color: var(--red); font-weight: 900; text-align: center;
  }
  .feature.hours { left: 396px; }
  .feature.hours .big { font-size: 46px; line-height: 1.1; }
  .feature.hours .small { font-size: 44px; line-height: 1.1; }
  .feature.auto { left: 614px; font-size: 31px; line-height: 1.3; }
  .footer {
    position: absolute; left: 0; top: 978px; width: 848px; height: 222px; background: var(--white);
  }
  .footer-name {
    position: absolute; left: 28px; top: 26px; width: 792px; height: 100px;
    border: 5px solid var(--red); display: flex; align-items: center; justify-content: center; gap: 40px;
    color: var(--red); font-weight: 900; white-space: nowrap;
  }
  .footer-name .shop-name { font-size: 44px; }
  .footer-name .shop-kind { font-size: 58px; letter-spacing: 2px; }
  .address { position: absolute; left: 30px; top: 154px; font-weight: 700; font-size: 28px; color: var(--ink); }
  .map-note {
    position: absolute; left: 495px; top: 148px; width: 325px; height: 46px;
    background: var(--red); color: var(--white); font-weight: 700; font-size: 24px;
    display: flex; align-items: center; justify-content: center; white-space: nowrap;
  }
</style>
</head>
<body>
<main class="flyer">
  <div class="hero-photo" role="img" aria-label="青空を背景に白い洗濯物のかごを抱えた女性の写真"></div>

  <div class="date">6<span class="unit">月</span>6<span class="unit">日</span></div>
  <div class="weekday">金</div>
  <div class="open">OPEN</div>

  <section class="shop-banner">
    <div class="shop-name">さらり堂</div>
    <div class="shop-kind">コインランドリー</div>
  </section>

  <section class="sale-badge">
    <div class="until">6/30まで</div>
    <div class="scope">全機種</div>
    <div class="half">半額</div>
  </section>

  <div class="mascot" role="img" aria-label="キャラクター「ぴかりん」のイラスト"></div>
  <div class="mascot-name">ぴかりん</div>

  <div class="feature-band"></div>
  <div class="store-photo" role="img" aria-label="赤い屋根の店舗外観の写真"></div>
  <div class="feature hours"><span class="big">24時間</span><span class="small">営業</span></div>
  <div class="feature auto">全自動<br>洗濯乾燥機<br>を導入</div>

  <footer class="footer">
    <div class="footer-name"><span class="shop-name">さらり堂</span><span class="shop-kind">コインランドリー</span></div>
    <div class="address">大分市椿原427-5</div>
    <div class="map-note">地図は裏面をご覧下さい。</div>
  </footer>
</main>
</body>
</html>
```